CalmVisit Homepage and Landing Pages

Please see detailed brief.

CalmVisit is Australia’s newest online therapy and mental health service. We allow patients from across australia to connect with Mental health practitioners from across Australia. Our mission is to remove the friction in gaining support for mental health related issues.

Number of Pages Required

1 page

Font styles to use
Sans Serif

Colors
33a6d7
0293ce
3277b5
0255a3
acd136
9bcb3c

Requirements
Must have
• Please see detailed brief.
Nice to have
• Please see detailed brief
Should not have

```html
<!DOCTYPE html>
<html lang="en">
<head>
<meta charset="utf-8">
<title>CalmVisit – Online Therapy and Mental Health Service</title>
<link rel="stylesheet" href="https://fonts.googleapis.com/css2?family=Quicksand:wght@500;600;700&family=Lato:wght@400;700&display=swap">
<style>
:root{
  --navy:#0a3f93;
  --blue:#1a7cc4;
  --blue-band:#1a80c6;
  --link:#3277b5;
  --green:#9bcb3c;
  --mist:#eef3f7;
  --ink:#222;
  --white:#fff;
}
*{box-sizing:border-box;margin:0;padding:0}
html,body{width:1200px;height:3471px;overflow:hidden;background:var(--white)}
body{position:relative;font-family:'Lato',sans-serif;color:var(--ink)}
.abs{position:absolute}
.head-font{font-family:'Quicksand',sans-serif}

/* header */
.site-header{left:0;top:0;width:1200px;height:77px;background:var(--white)}
.brand{left:58px;top:14px;display:flex;align-items:center;gap:14px;font-family:'Quicksand',sans-serif;font-size:42px;font-weight:500;color:#333}
.brand-dot{width:30px;height:30px;border-radius:50%;background:var(--blue)}
.nav a{position:absolute;top:28px;font-family:'Quicksand',sans-serif;font-size:17px;font-weight:500;color:#333;text-decoration:none;white-space:nowrap}
.nav a.active{color:var(--blue)}

/* hero */
.hero-photo{left:0;top:77px;width:1200px;height:584px;background:linear-gradient(100deg,#efe7de 0%,#e6d8c8 35%,#c9b49a 60%,#aab7c9 80%,#c89b68 100%)}
.hero-title{left:104px;top:228px;font-family:'Quicksand',sans-serif;font-weight:700;font-size:56px;color:var(--navy);line-height:1}
.hero-sub{left:99px;top:296px;font-family:'Quicksand',sans-serif;font-weight:500;font-size:40px;line-height:45px;color:var(--link)}
.socials{left:101px;top:405px;display:flex;gap:12px}
.socials span{width:30px;height:30px;border-radius:50%;background:#222}
.btn{position:absolute;display:flex;align-items:center;justify-content:center;color:var(--white);text-decoration:none}
.btn-hero{font-family:'Quicksand',sans-serif;font-weight:700;font-size:19px;letter-spacing:1px}
.btn-card{font-size:19px}
.green{background:var(--green)}
.blue{background:var(--blue)}

/* feature cards */
.photo{position:absolute}
.card{position:absolute}
.card h2{position:absolute;font-family:'Quicksand',sans-serif;font-weight:500;font-size:39px;white-space:nowrap}
.card .copy{position:absolute;font-size:17px;line-height:22px}
.card .copy p{margin-bottom:12px}
.card-navy{background:var(--navy);color:var(--white)}
.card-navy .copy{font-size:15.5px;line-height:27px}
.card-mist{background:var(--mist);color:var(--ink)}
.card-mist h2{color:var(--navy)}
.card-green{background:var(--green);color:var(--white)}

/* contact */
.contact-left{left:0;top:2838px;width:412px;height:540px;background:var(--navy);color:var(--white)}
.contact-right{left:412px;top:2838px;width:788px;height:540px;background:var(--blue-band)}
.contact-left h2{position:absolute;left:77px;top:100px;font-family:'Quicksand',sans-serif;font-weight:500;font-size:38px}
.contact-left p{position:absolute;left:77px;font-size:17px;line-height:31px}
.field{position:absolute;border-bottom:2px solid rgba(255,255,255,.85);color:var(--white);font-size:17px;padding-bottom:6px}
.submit{left:505px;top:3254px;width:500px;height:52px;font-size:19px}

.footer-note{left:0;top:3412px;width:1200px;text-align:center;font-size:15px;color:#333}
</style>
</head>
<body>

<header class="abs site-header">
  <div class="abs brand"><span class="brand-dot"></span>CalmVisit</div>
  <nav class="nav">
    <a class="active" style="left:431px" href="#">Home</a>
    <a style="left:533px" href="#">About Us</a>
    <a style="left:661px" href="#">Our Team</a>
    <a style="left:796px" href="#">Contact</a>
  </nav>
</header>

<section>
  <div class="abs hero-photo" role="img" aria-label="Older woman on a couch holding a tablet during a video session with a therapist"></div>
  <h1 class="abs hero-title">CalmVisit</h1>
  <p class="abs hero-sub">Online Therapy and<br>Mental Health Service</p>
  <div class="abs socials"><span></span><span></span><span></span><span></span></div>
  <a class="btn btn-hero green" style="left:671px;top:621px;width:265px;height:86px" href="#">BOOK THREAPY</a>
  <a class="btn btn-hero blue" style="left:936px;top:621px;width:264px;height:86px" href="#">MEET OUR TEAM</a>
</section>

<section>
  <div class="photo" style="left:141px;top:772px;width:648px;height:465px;background:linear-gradient(120deg,#8a8a88,#cfc6b8 50%,#7d6a55)" role="img" aria-label="Patient holding a tablet on a video call with a doctor"></div>
  <div class="card card-navy" style="left:560px;top:889px;width:511px;height:435px">
    <h2 style="left:58px;top:86px">What is CalmVisit</h2>
    <div class="copy" style="left:61px;top:145px;width:420px">CalmVisit is Australia’s newest online therapy and mental health service. We allow patients from across australia to connect with Mental health practitioners from across Australia. Our mission is to remove the friction in gaining support for mental health related issues.</div>
  </div>
  <a class="btn btn-card blue" style="left:560px;top:1255px;width:213px;height:69px" href="#">LEARN MORE</a>
</section>

<section>
  <div class="photo" style="left:408px;top:1417px;width:792px;height:556px;background:linear-gradient(110deg,#6b4a3a,#e2dedb 35%,#f1f1f1 70%,#d9d9d9)" role="img" aria-label="Woman at a laptop speaking with a smiling doctor on video"></div>
  <div class="card card-mist" style="left:137px;top:1650px;width:588px;height:435px">
    <h2 style="left:68px;top:80px">Find the help you need</h2>
    <div class="copy" style="left:68px;top:150px;width:450px">
      <p>Book an appointment with one of our highly qualified, licensed practitioners.</p>
      <p>The consultation can be conducted from wherever you feel most comfortable.</p>
      <p>No travel. No Clinics.</p>
    </div>
  </div>
  <a class="btn btn-card green" style="left:512px;top:2016px;width:213px;height:69px" href="#">LEARN MORE</a>
</section>

<section>
  <div class="photo" style="left:148px;top:2201px;width:648px;height:463px;background:linear-gradient(120deg,#d8d4cc,#eceae6 50%,#c9d3de)" role="img" aria-label="Senior doctor in a white coat with a stethoscope, seated at a desk"></div>
  <div class="card card-green" style="left:567px;top:2317px;width:511px;height:435px">
    <h2 style="left:55px;top:68px">Practitioner</h2>
    <div class="copy" style="left:55px;top:140px;width:410px">
      <p>CalmVisit allows GP's &amp; mental health practitioners from across Australia to connect and treat patients country wide.</p>
      <p>If you have over 10 years experience and a valid practicing license, sign up below and become a CalmVisit today.</p>
    </div>
  </div>
  <a class="btn btn-card blue" style="left:567px;top:2687px;width:198px;height:65px" href="#">LEARN MORE</a>
</section>

<section>
  <div class="abs contact-left">
    <h2>Contact Us</h2>
    <p style="top:168px">For a little more privacy, email me<br>directly at the following email...</p>
    <p style="top:244px">(555) 014 2386</p>
    <p style="top:288px">hello@calmvisit.example</p>
  </div>
  <div class="abs contact-right"></div>
  <div class="field" style="left:505px;top:2950px;width:237px">First Name</div>
  <div class="field" style="left:769px;top:2950px;width:236px">Last Name</div>
  <div class="field" style="left:505px;top:3039px;width:237px">Email</div>
  <div class="field" style="left:769px;top:3039px;width:236px;padding-left:8px">Phone</div>
  <div class="field" style="left:505px;top:3128px;width:500px;height:94px">Type Message here</div>
  <a class="btn submit green" href="#">SUBMIT</a>
</section>

<footer class="abs footer-note">© 2020 Company Name | All Rights Reserved</footer>

</body>
</html>
```